New York Property Management Company needs a Brochure Designed

We need a brochure for a new property management company in New York called KT7 Realty Partners. The 2 is superscript (squared.) We are looking for buildings to manage and want to showcase our expertise and caring. Logo is attached. We are getting a different photo and do not need all the verbiage. Also, does not need to be a trifold.
Updates

Property management group is a RESIDENTIAL property management group. I neglected to mention that. Thanks.

Hi designers, We've received very few designs so far so we've extended the deadline. We're hoping to receive your creative submissions soon! Thank you!

Reason: A few people have to weigh in on the design and it has been difficult coordinating this. We are getting close to making a decision and just need a few more days.

Industry/Entity Type

Property Management

```html
<!DOCTYPE html>
<html lang="en">
<head>
<meta charset="utf-8">
<title>About Us – KT7 Realty Partners</title>
<link rel="stylesheet" href="https://fonts.googleapis.com/css2?family=Didact+Gothic&family=Montserrat:wght@700;800&display=swap">
<style>
  :root {
    --band-dark: #3b3331;
    --panel-grey: #5b5a5a;
    --brand-box: #6e6d6d;
    --rule-white: #f2f2f2;
    --text-light: #f4f4f4;
    --sky-deep: #4f6a80;
    --sky-light: #d3dde4;
  }
  * { margin: 0; padding: 0; box-sizing: border-box; }
  html, body { width: 1200px; height: 600px; overflow: hidden; background: var(--band-dark); }
  .brochure-page {
    position: relative;
    width: 1200px;
    height: 600px;
    overflow: hidden;
    font-family: "Didact Gothic", "Century Gothic", sans-serif;
    color: var(--text-light);
  }
  .about-column {
    position: absolute;
    left: 0; top: 0;
    width: 600px; height: 600px;
    background: var(--panel-grey);
  }
  .about-header {
    position: absolute;
    left: 0; top: 0;
    width: 600px; height: 86px;
    background: var(--band-dark);
    border-bottom: 4px solid var(--rule-white);
  }
  .about-title {
    position: absolute;
    left: 25px; top: 20px;
    font-family: "Montserrat", "Century Gothic", sans-serif;
    font-weight: 800;
    font-size: 37px;
    letter-spacing: 0.5px;
    color: var(--text-light);
  }
  .brand-mark {
    position: absolute;
    right: 0; top: 0;
    width: 88px; height: 86px;
    background: var(--brand-box);
    display: flex;
    flex-direction: column;
    align-items: center;
    justify-content: center;
    text-align: center;
    font-size: 12px;
    line-height: 14px;
    letter-spacing: 1px;
    color: var(--text-light);
  }
  .about-copy {
    position: absolute;
    left: 18px; top: 144px;
    width: 574px;
    font-size: 15px;
    line-height: 18px;
    hyphens: auto;
  }
  .about-copy p + p { margin-top: 18px; }
  .skyline-photo {
    position: absolute;
    left: 600px; top: 0;
    width: 600px; height: 389px;
    background: linear-gradient(200deg, var(--sky-light) 0%, #8fa5b5 45%, var(--sky-deep) 100%);
  }
  .team-panel {
    position: absolute;
    left: 600px; top: 389px;
    width: 600px; height: 211px;
    background: var(--band-dark);
  }
  .team-copy {
    position: absolute;
    left: 40px; top: 58px;
    width: 535px;
    font-size: 15px;
    line-height: 18px;
  }
</style>
</head>
<body>
  <main class="brochure-page">
    <section class="about-column">
      <header class="about-header">
        <h1 class="about-title">ABOUT US</h1>
        <div class="brand-mark">KT7<br>REALTY<br>PARTNERS</div>
      </header>
      <div class="about-copy">
        <p>At KT7 Realty Partners, we manage each building as if it were our own; return each phone call; respond to each email; negotiate the best possible pricing on goods and services; address building needs in a respectful, practical, efficient and economic manner.</p>
        <p>We manage buildings with the highest level of service. Management is about service; it is knowing the operations of a building, but it is so much more. It is understanding resident and owner needs, identifying opportunities for creating value and providing a well-run and supportive community.</p>
        <p>Management encompasses all building services including, but not limited to, billing, collections, staff management, maintenance, compliance, capital projects and communication with owners, residents, vendors and building professionals. We do this by using established, reputable and reliable business partners.</p>
      </div>
    </section>
    <div class="skyline-photo" role="img" aria-label="Upward view of glass office towers against a pale sky"></div>
    <section class="team-panel">
      <p class="team-copy">In order for our philosophy to succeed, a manager must be more than just an employee. KT7RP provides growth opportunities that motivate staff for long-term potential and retention. The team is important for sharing of expertise, knowledge and experience. We are engaged as a team on each and every property.</p>
    </section>
  </main>
</body>
</html>
```